High Quality Hemp Flowers Packaging Design

We need a logo and packaging design for a new CBD hemp product. We sell CBD rich hemp flower- tops to our customers in Europe. CBD's natural benefits are extensive and generally used for all sorts of reasons.
Our strains are of the highest quality and used as an aromatic product. Thus the design should look clean and modern with a slight organic touch. We'd like people to associate our product with a luxury product like a good wine or whiskey but still being modern, healthy and organic.
The product comes in a brown cardboard paper tube and the design needs to include:
-our logo made of the "elvra sorrett" (attachment 1 elvra sorrett)
-our website: "vorim.eu"
-the product name: "elvra"
tube properties:
tube size: 6cm diameter, 7cm height (please see attachment 2 Paper Tube 6cm diameter, 7cm height. jpg)
• material: 2mm thickness cardboard+brown kraft paper (like in attachment 3 Paper Tube colour.jpg – picture just a sample for the material – size is not correctly displayed in this picture)
• coated aluminum foil paper inside
• colour/ product name: whatever colour and where ever you want to place it in your design
• colour/ tilda sorret logo: whatever colour and where ever you want to place it in your design
• sticker (2-2.5 x 5-6,5cm –> whatever the designer thinks works better) for sealing use, to keep the two parts of the tube together and it needs to have a placeholder for the date of the packaging (like in attachment 2 Paper Tube 6cm diameter 7cm height – but the sticker will not cover the full side of the tube as in attachment 2, but just 5-6.5 cm)
• “inner” tube could be color printing (for clarification which part please see attachment 3 Paper Tube colour.jpg -> the white part – picture just a sample for the “white part” – size is not correctly displayed in this picture
- We dont need any marihuana leafs or signs.

```html
<!DOCTYPE html>
<html lang="en">
<head>
<meta charset="utf-8">
<title>Elvra – Tube Label</title>
<link rel="stylesheet" href="https://fonts.googleapis.com/css2?family=Cormorant+Garamond:wght@600&family=Arimo:wght@400&display=swap">
<style>
  :root {
    --backdrop-light: #f3f3f3;
    --backdrop-dark: #c9c9c9;
    --label-black: #2a2a2a;
    --lid-black: #262626;
    --accent-red: #e2472b;
    --seam: #1c1c1c;
  }
  html, body {
    margin: 0;
    width: 1200px;
    height: 901px;
    overflow: hidden;
  }
  body {
    background: radial-gradient(ellipse at center, var(--backdrop-light) 0%, var(--backdrop-dark) 100%);
    position: relative;
  }
  .tube-label {
    position: absolute;
    left: 320px;
    top: 50px;
    width: 560px;
    height: 790px;
    background: var(--label-black);
    overflow: hidden;
  }
  .lid {
    position: absolute;
    left: 0; top: 0;
    width: 100%;
    height: 280px;
    background: var(--lid-black);
    border-bottom: 3px solid var(--seam);
  }
  .red-band {
    position: absolute;
    left: 0; top: 510px;
    width: 100%;
    height: 280px;
    background: var(--accent-red);
  }
  .emblem-frame {
    position: absolute;
    left: 0; top: 0;
    width: 560px;
    height: 790px;
  }
  .brand-mark {
    position: absolute;
    left: 0; top: 352px;
    width: 100%;
    text-align: center;
    color: var(--accent-red);
    font-family: "Cormorant Garamond", serif;
    font-weight: 600;
    font-size: 22px;
    line-height: 1.2;
    letter-spacing: 3px;
  }
  .brand-mark .dot {
    display: block;
    width: 22px;
    height: 22px;
    margin: 0 auto 6px;
    border: 3px solid var(--accent-red);
    border-radius: 50%;
  }
  .product-name {
    position: absolute;
    left: 0; top: 498px;
    width: 100%;
    margin: 0;
    text-align: center;
    color: var(--accent-red);
    font-family: "Cormorant Garamond", serif;
    font-weight: 600;
    font-size: 92px;
    line-height: 1;
    letter-spacing: 2px;
  }
  .website {
    position: absolute;
    left: 220px; top: 722px;
    width: 120px;
    height: 36px;
    border-radius: 18px;
    background: var(--label-black);
    color: var(--accent-red);
    font-family: "Arimo", sans-serif;
    font-size: 20px;
    line-height: 36px;
    text-align: center;
  }
</style>
</head>
<body>
  <main class="tube-label">
    <div class="lid"></div>
    <div class="red-band"></div>
    <svg class="emblem-frame" viewBox="0 0 560 790" aria-hidden="true">
      <rect x="55" y="440" width="455" height="215" rx="107" ry="107"
            fill="var(--label-black)" stroke="var(--accent-red)" stroke-width="6"/>
      <rect x="80" y="462" width="405" height="171" rx="85" ry="85"
            fill="none" stroke="var(--accent-red)" stroke-width="3"/>
    </svg>
    <div class="brand-mark"><span class="dot"></span>ELVRA SORRETT</div>
    <h1 class="product-name">ELVRA</h1>
    <div class="website">vorim.eu</div>
  </main>
</body>
</html>
```